Meridel Haulage - Website

A clean, not cluttered informative website for our business. We specialize in the transportation of radioactive materials across North America. The site is mostly for information about our company and will not be used to attract business but will be used to attract employee's mainly drivers. Driver's are very hard to find in our area. One of the pages needs to be a job's posting page with an apply now button. Either an application can be filled out there or a resume can be uploaded which ever functionality works better. I would like a website that I can easily edit, ability to change text and photos.

Number of Pages Required

5+ page

Colors

Designer to choose colors to be used in the design.

Requirements
Must have
• Home - About - Services - Jobs - Contact pages
• A way prospective employee's can apply or upload their resume to be emailed to me
• Very clean apperance
Should not have
• I don't want it to be busy

```html
<!DOCTYPE html>
<html lang="en">
<head>
<meta charset="utf-8">
<title>Meridel Haulage – Home</title>
<link rel="stylesheet" href="https://fonts.googleapis.com/css2?family=Montserrat:wght@400;500;700;800&family=Rubik:wght@300;400&display=swap">
<style>
  :root {
    --navy: #172036;
    --navy-soft: rgba(28, 30, 40, 0.78);
    --orange: #f7821f;
    --white: #ffffff;
    --paper: #fbfbfa;
    --ink: #1c1f2a;
    --muted: #9a9ca3;
    --line: #e3e3e6;
  }
  * { box-sizing: border-box; margin: 0; padding: 0; }
  html, body { width: 1200px; height: 784px; overflow: hidden; background: var(--white); }
  body { font-family: "Montserrat", sans-serif; color: var(--ink); position: relative; }

  .hero { position: absolute; left: 0; top: 0; width: 1200px; height: 470px; background: var(--white); }
  .hero__navy { position: absolute; left: 0; top: 0; width: 600px; height: 470px; background: var(--navy); }
  .hero__phone { position: absolute; right: 100px; top: 22px; font-size: 10px; color: var(--ink); }
  .hero__photo { position: absolute; left: 98px; top: 56px; width: 1002px; height: 352px;
    background: linear-gradient(100deg, #3a2e24 0%, #6d543d 35%, #b68c5f 55%, #8d7a4c 75%, #4f5a30 100%); }
  .hero__panel { position: absolute; left: 98px; top: 56px; width: 502px; height: 352px; background: var(--navy-soft); padding: 110px 0 0 86px; }
  .hero__title { font-family: "Rubik", sans-serif; font-weight: 300; font-size: 46px; line-height: 1.04; color: var(--white); letter-spacing: 1px; }
  .hero__text { margin-top: 18px; width: 320px; font-size: 9px; line-height: 1.5; color: #e6e6e6; }
  .hero__button { margin-top: 20px; display: inline-flex; align-items: center; gap: 22px; height: 32px; padding: 0 24px;
    background: var(--orange); color: var(--white); font-size: 9px; font-weight: 500; }
  .hero__button span.arrow { display: block; width: 40px; height: 1px; background: var(--white); }
  .nav { position: absolute; left: 142px; top: 432px; display: flex; gap: 28px; list-style: none; }
  .nav li { font-size: 9px; font-weight: 700; color: var(--white); letter-spacing: .3px; }

  .about { position: absolute; left: 0; top: 470px; width: 1200px; height: 314px; background: var(--paper); }
  .about__heading { position: absolute; left: 100px; top: 42px; font-size: 24px; font-weight: 800; letter-spacing: 1px; }
  .about__brand { position: absolute; right: 140px; top: 28px; font-size: 32px; font-weight: 800; color: var(--orange); letter-spacing: 1px; }
  .about__tabs { position: absolute; left: 100px; top: 104px; list-style: none; }
  .about__tabs li { font-size: 10px; font-style: italic; color: var(--muted); height: 54px; }
  .about__tabs li.is-active { font-style: normal; font-weight: 700; color: var(--ink); padding-left: 52px; }
  .about__photo { position: absolute; left: 400px; top: 80px; width: 700px; height: 160px;
    background: linear-gradient(180deg, #cfd2d3 0%, #9ea4a6 45%, #5d5f5d 75%, #6f6a5e 100%); }
  .about__title { position: absolute; left: 400px; top: 262px; font-size: 11px; font-weight: 700; }
  .about__note { position: absolute; right: 100px; top: 262px; font-size: 9px; }
  .about__text { position: absolute; left: 400px; top: 284px; font-size: 9px; color: #555; }
</style>
</head>
<body>
  <header class="hero">
    <div class="hero__navy"></div>
    <p class="hero__phone">contact phone number</p>
    <div class="hero__photo" role="img" aria-label="Photo of a haulage truck cab driving on a highway at sunset"></div>
    <div class="hero__panel">
      <h1 class="hero__title">LOREM<br>IPSUM</h1>
      <p class="hero__text">Lorem ipsum dolor sit amet, consectetur adipiscing elit, sed do eiusmod tempor incididunt ut labore</p>
      <a class="hero__button">Contact us <span class="arrow"></span></a>
    </div>
    <ul class="nav">
      <li>HOME</li><li>ABOUT US</li><li>SERVICES</li><li>JOBS</li><li>CONTACT US</li>
    </ul>
  </header>

  <section class="about">
    <h2 class="about__heading">ABOUT US</h2>
    <p class="about__brand">Meridel Haulage</p>
    <ul class="about__tabs">
      <li>Title number<br>one</li>
      <li class="is-active">Title number<br>two</li>
      <li>Title number<br>three</li>
      <li>Title number four</li>
    </ul>
    <div class="about__photo" role="img" aria-label="Photo of a semi truck hauling cylindrical containers on a flatbed trailer"></div>
    <h3 class="about__title">TITLE NUMBER TWO</h3>
    <p class="about__note">note 1</p>
    <p class="about__text">Lorem ipsum dolor sit amet, consectetur adipiscing elit, sed do eiusmod</p>
  </section>
</body>
</html>
```